Australian Independent Feature Film SPITE needs poster design

Here is the story of the film: SPITE tells the story of an Indian man named Kal who gets deeper and deeper involved in the Australian gangland underworld. He becomes close to his mentor The Lamplighter Otto and becomes emotionally involved with Otto's niece Tessa. His relationship with Tessa makes him an enemy of Max, Tessa's "partner" and Otto's right hand man. Kal only wants to get enough money to go back to homeland to rescue his parents from abject poverty, but is forced by Otto and Tessa to make increasing difficult decisions that go against what's left of his conscience. His confrontations with Max don't help. How far is too far when one tries to reach his noble goal? SPITE is an epic film tribute to Gerald Hume Wexley's The Lamplighter, a story of family relationships, intrigues and betrayals set against a violent world where nothing is legal, but where everything is possible.

The attached photos are to give you inspiration to create the poster. There is also attached a word document that includes the film credits that need to be in the poster.

Target Market(s)

international English speaking audiences. The poster should be very classy and appeal to audiences who like very artistic and something different in their films - not the usual commercial superhero films that are flooding the market now. I've attached some film posters from The Lamplighter, Ironjaw and other films as references.

Industry/Entity Type

Film Production

Font styles to use
Other font styles liked:
• HYPMoKGaK-Bold-Italics for Main Title SPITE is an option, but not absolutely necessary. The font seems to have bullet holes through it and is torn along edges.

Colors

Designer to choose colors to be used in the design.

Requirements
Must have
• There is attached a word document that includes the film credits that need to be in the poster.
Nice to have
• images that are highly dramatic and eye catching
Should not have
• Should not have any images that include nudity. This should be a poster for all audiences.

```html
<!DOCTYPE html>
<html lang="en">
<head>
<meta charset="utf-8">
<title>SPITE – Film Poster</title>
<link rel="stylesheet" href="https://fonts.googleapis.com/css2?family=Oswald:wght@400;500&family=Rubik+Dirt&family=Libre+Baskerville:wght@700&display=swap">
<style>
  :root {
    --mat: #eceeed;
    --blood: #8c0d0e;
    --blood-mid: #7a0a0b;
    --blood-deep: #5a0607;
    --blood-dark: #3a0405;
    --ink-dark: #2a0405;
    --credit: #f1d9d9;
    --paper: #ffffff;
  }
  * { margin: 0; padding: 0; box-sizing: border-box; }
  html, body { width: 928px; height: 1200px; overflow: hidden; background: var(--mat); }
  .poster {
    position: absolute; left: 131px; top: 129px; width: 665px; height: 941px;
    background:
      radial-gradient(circle at 12% 18%, rgba(58,4,5,0.45) 0%, rgba(58,4,5,0) 22%),
      radial-gradient(circle at 88% 70%, rgba(58,4,5,0.4) 0%, rgba(58,4,5,0) 20%),
      radial-gradient(circle at 20% 88%, rgba(58,4,5,0.35) 0%, rgba(58,4,5,0) 18%),
      radial-gradient(circle at 70% 12%, rgba(160,20,20,0.35) 0%, rgba(160,20,20,0) 25%),
      radial-gradient(ellipse at 50% 45%, var(--blood) 0%, var(--blood-mid) 50%, var(--blood-deep) 88%, var(--blood-dark) 100%);
    overflow: hidden;
  }
  .presenters {
    position: absolute; top: 69px; left: 0; width: 100%; text-align: center;
    font-family: "Oswald", sans-serif; font-weight: 500; font-size: 13px;
    letter-spacing: 0.2px; color: var(--ink-dark); line-height: 1;
  }
  .presents { top: 105px; }
  .profile-art {
    position: absolute; left: 202px; top: 251px; width: 267px; height: 390px;
    border-radius: 48% 44% 34% 24% / 34% 32% 22% 14%;
    background: linear-gradient(180deg, #ffffff 0%, #f4eeee 100%);
  }
  .profile-mark {
    position: absolute; left: 262px; top: 252px; width: 150px; height: 215px;
    display: flex; align-items: center; justify-content: center;
    font-family: "Libre Baskerville", serif; font-weight: 700; font-size: 210px;
    line-height: 1; color: var(--blood);
  }
  .title {
    position: absolute; top: 700px; left: 0; width: 100%; text-align: center;
    font-family: "Rubik Dirt", sans-serif; font-size: 116px; line-height: 1;
    letter-spacing: 6px; color: var(--paper);
  }
  .byline {
    position: absolute; top: 804px; left: 0; width: 100%; text-align: center;
    font-family: "Libre Baskerville", serif; font-weight: 700; font-size: 12px;
    color: var(--paper);
  }
  .billing {
    position: absolute; top: 829px; left: 100px; width: 465px; text-align: center;
    font-family: "Oswald", sans-serif; font-size: 7.6px; line-height: 12.5px;
    color: var(--credit); white-space: nowrap;
  }
  .billing .role { font-weight: 500; text-transform: uppercase; color: var(--paper); }
</style>
</head>
<body>
  <main class="poster">
    <p class="presenters">HARBOURLINE PICTURES PTY LTD &amp; REDGUM PRODUCTIONS PTY LTD</p>
    <p class="presenters presents">PRESENTS</p>

    <div class="profile-art" role="img" aria-label="White silhouette of a man's head in profile with a red dollar sign pierced by a screw inside it"></div>
    <span class="profile-mark" aria-hidden="true">$</span>

    <h1 class="title">SPITE</h1>
    <p class="byline">A Marlowe Quinn Film</p>

    <div class="billing">
      <p>Harbourline Pictures and Redgum Productions present a Marlowe Quinn film SPITE <span class="role">starring</span> Ash Varma Rosa Dean Kit Holm Lena Fry Ned Sharpe</p>
      <p>Ivy Lund Paul Roche Ben Carr Dale Wick <span class="role">producers</span> Ash Varma &amp; Marlowe Quinn <span class="role">associate producers</span> Nell Grady &amp; Tom Vale</p>
      <p><span class="role">director of photography &amp; editor</span> Sam Ortiz <span class="role">post-production supervisor</span> Cleo Bain <span class="role">re-recording mixer &amp; sound design</span> Reid Moss</p>
      <p><span class="role">music composer</span> Owen Pratt <span class="role">production design</span> Lara Voss <span class="role">costume design</span> Mia Stone <span class="role">makeup &amp; hair design</span> Jude Finch</p>
      <p><span class="role">casting</span> Redgum Productions <span class="role">screenplay</span> Robin Hale <span class="role">directed by</span> Marlowe Quinn</p>
    </div>
  </main>
</body>
</html>
```